Hydroponic Farm Needs a Business Card

We need a business card design for a hydroponic farm located on the Gulf Coast called 'Tallowbend Farms'. We grow many forms of lettuce and tomatoes along with other herbs and spices. We currently sell to farmer's markets though will soon be expanding to commercial accounts such as restaurants and grocery stores. The colors should be bright and vibrant to reflect the nature of our produce. The final design should communicate a professional, clean, yet friendly impression and able to be used both with farmer's markets and commercial accounts.

The pictures are an example of our product. The pictures do not have to be incorporated into the business card design.

Please put areas for information such as Names, Phone Number, E-mail address, and additional information.

Industry/Entity Type

Farm

```html
<!DOCTYPE html>
<html lang="en">
<head>
<meta charset="utf-8">
<title>Tallowbend Farms – Business Card</title>
<link href="https://fonts.googleapis.com/css2?family=Open+Sans:wght@400;600;700&display=swap" rel="stylesheet">
<style>
  :root {
    --page-bg: #e9e7e3;
    --card-bg: #f4f4f4;
    --brand-blue: #2a8fd0;
    --deep-navy: #1d4a6e;
    --mid-navy: #2f5d82;
    --ink: #1d3f5c;
    --white: #ffffff;
  }
  * { box-sizing: border-box; margin: 0; padding: 0; }
  html, body {
    width: 1200px; height: 704px; overflow: hidden;
    background: var(--page-bg);
    font-family: "Open Sans", Arial, sans-serif;
  }
  .sheet {
    position: relative; width: 1200px; height: 704px;
    display: flex; align-items: center; justify-content: center; gap: 50px;
  }
  .card {
    position: relative; width: 525px; height: 300px;
    background: var(--card-bg);
    box-shadow: 0 6px 18px rgba(0,0,0,.18);
    overflow: hidden;
  }
  .card-texture {
    position: absolute; inset: 0;
    background: linear-gradient(135deg, #f7f7f7, #ececec);
  }
  .wordmark {
    position: absolute; display: flex; align-items: center; gap: 10px;
    color: var(--brand-blue); font-weight: 700; letter-spacing: .2px;
  }
  .wordmark-dot {
    width: 16px; height: 16px; border-radius: 50%; background: var(--brand-blue);
  }
  .card-front .wordmark { right: 40px; bottom: 70px; font-size: 34px; }

  .card-back .wordmark { left: 30px; top: 36px; font-size: 30px; }
  .name-band {
    position: absolute; right: 0; top: 96px; width: 270px;
  }
  .name-band .person-name {
    background: var(--brand-blue); color: var(--white);
    font-size: 27px; font-weight: 400; letter-spacing: 1px;
    padding: 4px 16px; text-transform: uppercase;
  }
  .name-band .person-title {
    background: var(--deep-navy); color: var(--white);
    font-size: 13px; letter-spacing: 3px; text-transform: uppercase;
    padding: 5px 16px;
  }
  .contact-band {
    position: absolute; left: 0; right: 0; bottom: 30px; height: 58px;
    background: var(--mid-navy); color: var(--white);
    font-size: 11px; letter-spacing: .5px;
    display: flex; justify-content: space-between; align-items: center;
    padding: 0 24px;
  }
  .contact-col { display: flex; flex-direction: column; gap: 8px; }
  .contact-line { display: flex; align-items: center; gap: 8px; }
  .contact-line svg { width: 12px; height: 12px; fill: var(--white); flex: none; }
  .web-line { text-transform: uppercase; }
</style>
</head>
<body>
<main class="sheet">
  <section class="card card-front" aria-label="Card front">
    <div class="card-texture" role="img" aria-label="Soft quilted diamond texture"></div>
    <div class="wordmark"><span class="wordmark-dot"></span>Tallowbend Farms</div>
  </section>

  <section class="card card-back" aria-label="Card back">
    <div class="card-texture" role="img" aria-label="Soft quilted diamond texture"></div>
    <div class="wordmark"><span class="wordmark-dot"></span>Tallowbend Farms</div>

    <div class="name-band">
      <p class="person-name">Lena Marsh</p>
      <p class="person-title">Executive Director</p>
    </div>

    <div class="contact-band">
      <div class="contact-col">
        <p class="contact-line">
          <svg viewBox="0 0 24 24"><path d="M6.6 10.8a15.1 15.1 0 0 0 6.6 6.6l2.2-2.2a1 1 0 0 1 1-.25 11.4 11.4 0 0 0 3.6.57 1 1 0 0 1 1 1V20a1 1 0 0 1-1 1A17 17 0 0 1 3 4a1 1 0 0 1 1-1h3.5a1 1 0 0 1 1 1c0 1.25.2 2.45.57 3.57a1 1 0 0 1-.25 1z"/></svg>
          +1 228 555 014 | +1 228 555 027
        </p>
        <p class="contact-line web-line">
          <svg viewBox="0 0 24 24"><circle cx="12" cy="12" r="10" fill="none" stroke="#fff" stroke-width="2"/><path d="M2 12h20M12 2c3 3 3 17 0 20M12 2c-3 3-3 17 0 20" fill="none" stroke="#fff" stroke-width="2"/></svg>
          www.tallowbendfarms.com
        </p>
      </div>
      <div class="contact-col">
        <p class="contact-line">
          <svg viewBox="0 0 24 24"><path d="M12 2a7 7 0 0 0-7 7c0 5 7 13 7 13s7-8 7-13a7 7 0 0 0-7-7zm0 9.5A2.5 2.5 0 1 1 12 6.5a2.5 2.5 0 0 1 0 5z"/></svg>
          Shoreline Rd, Gulfport, United States 39501
        </p>
        <p class="contact-line web-line">
          <svg viewBox="0 0 24 24"><path d="M2 5h20v14H2z" fill="none" stroke="#fff" stroke-width="2"/><path d="M2 5l10 8 10-8" fill="none" stroke="#fff" stroke-width="2"/></svg>
          hello@tallowbendfarms.com
        </p>
      </div>
    </div>
  </section>
</main>
</body>
</html>
```